Home page design for community learning promoters' website

There are about 3,000 community learning centers where people from underprivileged / marginalized communities can learn about basic technology topics like: how to use computers, how to use Internet (create an email, join and use social networks, etc.), how to use Word, Excel, PowerPoint, and so on... This is very useful for them because it gives them opportunities to find / get a better job and improve their standard of living.

Well, this website is an online community for those men and women (the promoters) who are responsible for leading the centers. They coordinate all the activities in the centers and they teach their students.

The website has two main objectives: 1) create culture about the importance of the promoters role in their communities and 2) create a place where promoters can learn, take online courses and share best practices.

The first objective is the "public" part of the website (homepage and public information) and the second one is the "private" part which is a pinwheel like online community (accessible only for registered users).

What we need is a fresh and modern visual design for 1) "public" homepage and 2) "private" homepage. I am attaching some mockups for the homepage "public" part (two different options) and for the main page of the "private" part (the pinwheel like online community). This doesn't mean that your design should be like those mockups, but they could be a guide for you to get ideas and better understend the website objectives. What we need is innovation.

The project scope is to design the home page for the "public" part and the home page for the "private" part. If you have any question, please ask me.

Target Market(s)

Target market (promoters) are 20-40 years old, they work from 4 to 8 hours in the centers and their connections are mainly satellital 256Kb/s

Industry/Entity Type

Internet

Requirements
Must have
• Spanish labeling. Find below what homepage must have. I include english / spanish versions. For sample text you can use "lorem ipsum". If you need help with spanish tranlations you can ask me.

The homepage must have:

Links / menu to main sections:
- Who we are / Quiénes somos
- What we do / Qué hacemos
- Our impact / Nuestro impacto
- Enter now! / ¡Ingresa ahora!

Benefits that the site offer to the promoters (why they should join the online community). Call-to-action should be "Join now / Regístrate ahora"
- Get trained (Take online courses and get access to more than 450 learning resources) / Capacítate (Toma cursos en línea y accede a más de 450 recursos de aprendizaje)
- Get certified (Approve the course and become a certified promoter) / Certifícate (Aprueba el curso y conviértete en un promotor certificado)
- Connect (Connect and work with more than 3,000 promoters around the country) / Conéctate (Conéctate y colabora con más de 3,000 promotores de todo el país)
- Share (Learn and share information with other promoters) / Comparte (Aprende y comparte información con otros promotores)

Links / blocks / menus to secondary sections:
- Success stories / Historias de éxito
- Events and contests / Concursos y eventos
- News or Featured news / Noticias destacadas
- Follow us on... (social networks like pinwheel, glimmo, quorvaSt, etc.) / Síguenos en...
- Frequently asked questions / Preguntas frecuentes
- Contact us / Contáctanos
- Site map / Mapa del sitio
- Privacy policy / Políticas de privacidad
- Terms and conditions of use / Términos y condiciones de uso

Also should include statistics like:
- More that 3,000 promoters / Más de 3,000 promotores
- More than 850 learning resources / Más de 850 recursos de aprendizaje
- More than 450,000 students / Más de 450,000 estudiantes

```html
<!DOCTYPE html>
<html lang="es">
<head>
<meta charset="utf-8">
<title>Aula Guía — Inicio</title>
<link href="https://fonts.googleapis.com/css2?family=Exo+2:wght@300;400;600;700;800&family=Pathway+Gothic+One&display=swap" rel="stylesheet">
<style>
:root{
  --blue:#0d63c8;
  --blue-dark:#0a54ad;
  --blue-text:#1166c4;
  --orange:#f7850f;
  --white:#ffffff;
  --grey-text:#8a8f99;
  --rule:#e3e6ea;
}
*{margin:0;padding:0;box-sizing:border-box}
html,body{width:1164px;height:1200px;overflow:hidden;background:var(--white);font-family:'Exo 2',sans-serif}
.page{position:relative;width:1164px;height:1200px;overflow:hidden}
.abs{position:absolute}

/* header */
.hero{left:0;top:0;width:1164px;height:375px;background:linear-gradient(180deg,#0f6bd2,#0b5dc0);box-shadow:0 4px 10px rgba(0,0,0,.18)}
.brand{left:194px;top:0;width:114px;height:88px;background:var(--white);box-shadow:0 3px 6px rgba(0,0,0,.2);display:flex;flex-direction:column;align-items:center;justify-content:center;gap:6px}
.brand-mark{width:22px;height:22px;background:var(--blue)}
.brand-name{font-weight:800;font-size:15px;line-height:15px;color:var(--orange);text-align:center}
.nav{left:350px;top:64px;display:flex;gap:0}
.nav a{color:var(--white);text-decoration:none;font-weight:600;font-size:15px;padding:0 11px;border-left:1px dotted rgba(255,255,255,.4);height:20px;line-height:20px}
.nav a:first-child{border-left:none;padding-left:2px}
.nav a.active{border-bottom:3px solid var(--orange);height:24px}
.account{left:782px;top:16px;font-size:10px;font-weight:700;color:var(--white);display:flex;gap:8px;align-items:center}
.account svg{vertical-align:-1px;margin-right:3px}
.cta{left:838px;top:52px;width:132px;height:36px;background:linear-gradient(#ff9a22,#f47a07);border:1px solid #ffb357;color:var(--white);font-weight:800;font-size:14px;display:flex;align-items:center;justify-content:center}
.arrow{width:28px;height:28px;background:var(--orange);display:flex;align-items:center;justify-content:center}
.quote{left:196px;top:154px;width:440px;font-family:'Pathway Gothic One',sans-serif;font-size:31px;line-height:38px;color:#cfe2fa;text-transform:uppercase;letter-spacing:-.5px}
.author{left:196px;top:272px;font-weight:800;font-size:19px;color:var(--white);letter-spacing:-.5px}
.hero-photo{left:650px;top:40px;width:260px;height:335px;background:radial-gradient(ellipse at 50% 35%,#c9cfd8 0 18%,#2f4c7c 40%,rgba(13,99,200,0) 72%)}

/* stats */
.stats-band{left:0;top:375px;width:1164px;height:122px;background:var(--white);box-shadow:0 10px 14px -10px rgba(0,0,0,.12)}
.stat{display:flex;align-items:center;gap:10px}
.stat-num{font-weight:800;font-size:21px;color:var(--orange);line-height:20px}
.stat-label{font-weight:400;font-size:22px;color:var(--blue-text);line-height:22px}
.stat-divider{width:1px;height:54px;border-left:1px dotted #d0d4da}

/* content */
.section-title{font-weight:800;font-size:20px;color:var(--blue-text);letter-spacing:-.6px;line-height:20px}
.rule{height:1px;background:var(--rule)}
.more{font-weight:800;font-size:9.5px;color:var(--blue-text)}
.note{font-weight:300;font-size:11px;line-height:13px;color:var(--grey-text)}
.date{width:30px;height:30px;background:var(--blue);color:var(--white);text-align:center;font-weight:700;font-size:14px;line-height:14px;padding-top:3px}
.date small{display:block;font-size:7px;line-height:9px}
.sidebar-col{left:446px;top:497px;width:1px;height:548px;background:linear-gradient(#e6e8ec,#f4f5f7);box-shadow:2px 0 6px rgba(0,0,0,.05)}
.video{left:197px;top:553px;width:163px;height:110px;background:#1d1e20;border:1px solid #ccc}
.video-top{height:52px;background:#232426}
.video-bar{position:absolute;left:0;bottom:0;width:100%;height:6px;background:#333}
.video-bar i{display:block;width:70%;height:3px;margin-top:1px;background:#1a8ecf}
.play{left:67px;top:38px;width:28px;height:28px;border-radius:50%;background:#ddd;border:2px solid #aaa}
.news-title{font-weight:700;font-size:13px;line-height:15px;color:var(--orange)}
.news-body{font-weight:300;font-size:11px;line-height:13px;color:#8e95b2;width:190px}
.social{width:28px;height:28px;border-radius:50%}

/* footer */
.footer{left:0;top:1045px;width:1164px;height:155px;background:var(--blue)}
.foot-col{width:138px}
.foot-col h4{font-weight:600;font-size:14px;color:var(--white);padding-bottom:3px;border-bottom:1px dotted rgba(255,255,255,.6);margin-bottom:6px;white-space:nowrap}
.foot-col a{display:block;color:#dbe8fb;text-decoration:none;font-size:12px;line-height:17px;border-bottom:1px dotted rgba(255,255,255,.3);padding-top:1px}
.legal{left:196px;top:1173px;font-size:10px;color:#dbe8fb}
</style>
</head>
<body>
<div class="page">

  <header class="abs hero">
    <div class="abs hero-photo" role="img" aria-label="Retrato de un directivo con traje y brazos cruzados"></div>
    <div class="abs brand"><span class="brand-mark"></span><span class="brand-name">AULA<br>GUÍA</span></div>
    <nav class="abs nav">
      <a class="active" href="#">QUIÉNES SOMOS</a>
      <a href="#">QUÉ HACEMOS</a>
      <a href="#">NUESTRO IMPACTO</a>
    </nav>
    <div class="abs account">
      <span><svg width="9" height="10" viewBox="0 0 9 10"><rect x="0" y="4" width="9" height="6" fill="#fff"/><path d="M2 4V3a2.5 2.5 0 0 1 5 0v1" stroke="#fff" fill="none" stroke-width="1.4"/></svg>REGISTRARME</span>
      <span style="opacity:.6">/</span>
      <span><svg width="10" height="10" viewBox="0 0 10 10"><circle cx="5" cy="3" r="2.6" fill="#fff"/><path d="M0 10a5 4 0 0 1 10 0z" fill="#fff"/></svg>INICIARSESSION</span>
    </div>
    <div class="abs cta">¡INGRESA AHORA!</div>
    <div class="abs arrow" style="left:110px;top:160px"><svg width="16" height="14" viewBox="0 0 16 14"><path d="M15 7H3M8 1 2 7l6 6" stroke="#fff" stroke-width="2.6" fill="none"/></svg></div>
    <div class="abs arrow" style="left:1027px;top:160px"><svg width="16" height="14" viewBox="0 0 16 14"><path d="M1 7h12M8 1l6 6-6 6" stroke="#fff" stroke-width="2.6" fill="none"/></svg></div>
    <p class="abs quote">“El promotor ayuda al desarrollo de su comunidad ganando respeto y satisfacción personal”</p>
    <p class="abs author">DR. ERNESTO VALDIVIA.</p>
  </header>

  <section class="abs stats-band">
    <div class="abs stat" style="left:194px;top:42px">
      <svg width="52" height="46" viewBox="0 0 52 46"><circle cx="34" cy="11" r="9" fill="#f7850f"/><path d="M20 40c0-12 6-18 14-18s16 6 16 18z" fill="#f7850f"/><circle cx="18" cy="15" r="9" fill="#f7850f" stroke="#fff" stroke-width="2"/><path d="M2 45c0-12 7-19 16-19s16 7 16 19z" fill="#f7850f" stroke="#fff" stroke-width="2"/></svg>
      <div><div class="stat-num">+ 3,000</div><div class="stat-label">PROMOTORES</div></div>
    </div>
    <div class="abs stat-divider" style="left:432px;top:42px"></div>
    <div class="abs stat" style="left:481px;top:42px">
      <svg width="50" height="48" viewBox="0 0 50 48"><rect x="18" y="4" width="30" height="40" fill="#f7850f"/><rect x="24" y="12" width="18" height="3" fill="#fff"/><rect x="24" y="19" width="18" height="3" fill="#fff"/><rect x="24" y="26" width="18" height="3" fill="#fff"/><rect x="0" y="0" width="24" height="48" fill="#f47a07"/></svg>
      <div><div class="stat-num">+ 800</div><div class="stat-label">PUBLICACIONES</div></div>
    </div>
    <div class="abs stat-divider" style="left:746px;top:42px"></div>
    <div class="abs stat" style="left:792px;top:40px">
      <svg width="76" height="52" viewBox="0 0 76 52"><path d="M38 2 76 16 38 30 0 16z" fill="#f7850f"/><path d="M16 24v12c8 8 36 8 44 0V24L38 32z" fill="#f7850f"/><path d="M8 18v22" stroke="#f7850f" stroke-width="3"/><path d="M5 40h6l-3 12z" fill="#f7850f"/></svg>
      <div><div class="stat-num">+ 450,000</div><div class="stat-label">ALUMNOS</div></div>
    </div>
  </section>

  <div class="abs sidebar-col"></div>

  <!-- sidebar -->
  <h2 class="abs section-title" style="left:196px;top:515px">HISTORIAS DE ÉXITO.</h2>
  <div class="abs rule" style="left:194px;top:543px;width:246px"></div>
  <div class="abs video" role="img" aria-label="Reproductor de video de una historia de éxito">
    <div class="video-top"></div>
    <div class="abs play"></div>
    <div class="video-bar"><i></i></div>
  </div>
  <p class="abs note" style="left:196px;top:669px;width:200px">“Ser promotor me ha permitido ayudar a mi comunidad”.</p>
  <p class="abs more" style="left:195px;top:700px">VER MÁS... &gt;&gt;</p>
  <div class="abs rule" style="left:194px;top:718px;width:246px"></div>
  <h2 class="abs section-title" style="left:196px;top:731px">EVENTOS Y CONCURSOS.</h2>
  <div class="abs rule" style="left:194px;top:758px;width:246px"></div>
  <div class="abs" role="img" aria-label="Grupo de personas recostadas en círculo sobre el suelo" style="left:195px;top:769px;width:163px;height:102px;background:linear-gradient(135deg,#d9d6d2,#8c8a92 50%,#c7c3bf);border:1px solid #ccc"></div>
  <div class="abs date" style="left:195px;top:876px">26<small>JUNE</small></div>
  <p class="abs note" style="left:244px;top:877px;width:190px">2do seminario internacional para el desarrollo comunitario.</p>
  <p class="abs more" style="left:195px;top:913px">VER MÁS... &gt;&gt;</p>
  <div class="abs rule" style="left:194px;top:931px;width:250px"></div>
  <h2 class="abs section-title" style="left:196px;top:946px">CONÉCTATE CON<br>NOSOTROS.</h2>
  <div class="abs social" title="glimmo" aria-label="glimmo" style="left:195px;top:997px;background:#2aa9e0"></div>
  <div class="abs social" title="pinwheel" aria-label="pinwheel" style="left:225px;top:997px;background:#3b5998"></div>
  <div class="abs social" title="plusora" aria-label="plusora" style="left:255px;top:997px;background:#333"></div>
  <div class="abs social" title="vidlo" aria-label="vidlo" style="left:285px;top:997px;background:#86c9e6"></div>
  <div class="abs social" title="callisto" aria-label="callisto" style="left:315px;top:997px;background:#12a5e8"></div>

  <!-- featured -->
  <h2 class="abs section-title" style="left:506px;top:515px">DESTACADO EN RED COMUNAL.</h2>

  <div class="abs" role="img" aria-label="Retrato de un joven sonriente con saco" style="left:504px;top:566px;width:170px;height:107px;background:linear-gradient(120deg,#e9e4df,#9a8676 55%,#4a4a4e)"></div>
  <div class="abs date" style="left:696px;top:566px">26<small>JUNE</small></div>
  <p class="abs news-title" style="left:735px;top:566px">LOREM IPSUM DOLOR SIT<br>AMET.</p>
  <p class="abs news-body" style="left:697px;top:605px">consectetuer adipiscing elit, sed diam nonummy nibh euismod tincidunt utconsectetuer adipiscing elit utconsectetuer.</p>
  <p class="abs more" style="left:698px;top:664px">VER MÁS... &gt;&gt;</p>

  <div class="abs" role="img" aria-label="Retrato de un hombre maduro sonriente" style="left:504px;top:704px;width:160px;height:107px;background:radial-gradient(ellipse at 50% 45%,#b99a84 0 25%,#e5e5e5 60%,#f8f8f8)"></div>
  <div class="abs date" style="left:696px;top:704px">25<small>JUNE</small></div>
  <p class="abs news-title" style="left:735px;top:704px">LOREM IPSUM DOLOR SIT<br>AMET.</p>
  <p class="abs news-body" style="left:697px;top:743px">consectetuer adipiscing elit, sed diam nonummy nibh euismod tincidunt utconsectetuer adipiscing elit utconsectetuer.</p>
  <p class="abs more" style="left:698px;top:802px">VER MÁS... &gt;&gt;</p>

  <div class="abs" role="img" aria-label="Retrato de un joven de cabello rizado" style="left:504px;top:853px;width:170px;height:107px;background:linear-gradient(90deg,#1f3e78,#8a6a55 45%,#e8b98c)"></div>
  <div class="abs date" style="left:696px;top:853px">24<small>JUNE</small></div>
  <p class="abs news-title" style="left:735px;top:853px">LOREM IPSUM DOLOR SIT<br>AMET.</p>
  <p class="abs news-body" style="left:697px;top:892px">consectetuer adipiscing elit, sed diam nonummy nibh euismod tincidunt utconsectetuer adipiscing elit utconsectetuer.</p>
  <p class="abs more" style="left:698px;top:951px">VER MÁS... &gt;&gt;</p>

  <!-- footer -->
  <footer class="abs footer">
    <div class="abs foot-col" style="left:196px;top:20px"><h4>SOBRE NOSOTROS</h4><a href="#">Qué hacemos</a><a href="#">Quiénes somos</a><a href="#">Nuestro impacto</a></div>
    <div class="abs foot-col" style="left:393px;top:22px"><h4>INVOLÚCRATE</h4><a href="#">Historias de éxito</a><a href="#">Eventos y concursos</a><a href="#">Noticias</a></div>
    <div class="abs foot-col" style="left:581px;top:22px"><h4>MÁS INFORMACIÓN</h4><a href="#">Preguntas frecuentes</a><a href="#">Contáctanos</a></div>
    <div class="abs foot-col" style="left:775px;top:22px;width:195px"><h4>COPYRIGHT © 2013. RED COMUNAL</h4><a href="#" style="width:138px">Políticas de privacidad</a><a href="#">Términos y condiciones de uso</a><a href="#" style="width:138px">Mapa del sitio</a></div>
  </footer>
  <p class="abs legal">ABOUT US | CONTACT US | FAQ | PRIVACY POLICY | TERMS &amp; CONDITIONS</p>

</div>
</body>
</html>
```